Webpage for a treatment housing for young addicts.

I need a new design and files for my wordpress page. I need it to be more neat and clean. I need it to look professional with a starting page that will work as a navigation. I need like logo and phone number and such up top, a picture under it with one sentence as a slogan and under it 6 boxes to click to come to our different pages. Under it I want news etc.

Target Market(s)

Social services, employees and governements

Coding

Coded - Design and coding required

Font styles to use
Sans Serif

Colors
abd037
3176b5
9d9d9d
aaaaaa
f04a50

Requirements
Must have
• A nice design
Nice to have
• need it to look professional with a starting page that will work as a navigation. I need like logo and phone number and such up top, a picture under it with one sentence as a slogan and under it 6 boxes to click to come to our different pages. Under it I want news etc.
• today www.kolrev.se
• want more like www.tralvik.se or www.bersona.se
Should not have
• To many different colours and a messy design.

```html
<!DOCTYPE html>
<html lang="en">
<head>
<meta charset="utf-8">
<title>Kolrev</title>
<link rel="stylesheet" href="https://fonts.googleapis.com/css2?family=Poppins:wght@300;400;500;600;700&display=swap">
<style>
:root{
  --blue:#3176b5;
  --green:#abd037;
  --red:#f04a50;
  --grey:#9d9d9d;
  --grey-light:#aaaaaa;
  --text:#3d3d3d;
  --body:#555555;
  --line:#e6e6e6;
  --panel:#ebebeb;
}
*{box-sizing:border-box;margin:0;padding:0}
html,body{width:1200px;height:2169px;overflow:hidden;background:#fff}
body{position:relative;font-family:"Poppins",sans-serif;color:var(--text)}

/* header */
.site-header{position:absolute;left:0;top:0;width:1200px;height:75px;background:#fff}
.brand{position:absolute;left:111px;top:20px;display:flex;align-items:center;gap:10px}
.brand-mark{width:34px;height:34px;background:var(--blue);border-radius:4px}
.brand-name{font-size:30px;font-weight:600;color:var(--blue);line-height:1}
.call{position:absolute;left:570px;top:26px;display:flex;align-items:center;gap:8px;font-size:16px;color:#333;white-space:nowrap}
.call strong{font-weight:500}
.vsep{position:absolute;top:0;width:1px;height:75px;background:var(--line)}
.search{position:absolute;left:816px;top:26px;width:166px;height:25px;border-bottom:1px solid var(--line);font-size:10px;color:#999;padding-top:4px}
.search svg{position:absolute;right:4px;top:3px}
.menu{position:absolute;left:1018px;top:28px;display:flex;align-items:center;gap:9px;font-size:13px;color:#222}

/* hero */
.hero{position:absolute;left:0;top:75px;width:1200px;height:377px;background:linear-gradient(135deg,#3b3a34 0%,#6b5a46 35%,#8a6d52 55%,#3c4632 80%,#232823 100%)}
.hero-title{position:absolute;left:0;top:208px;width:1200px;text-align:center;color:#fff;font-weight:600;font-size:34px;line-height:52px;letter-spacing:.5px;text-shadow:0 2px 6px rgba(0,0,0,.5)}

/* navigation tiles */
.tiles{position:absolute;left:0;top:452px;width:1200px;height:223px;background:linear-gradient(180deg,#c9c9c9,#dcdcdc 60%,#e9e9e9)}
.tile{position:absolute;width:309px;height:51px;background:#a7a7a7;box-shadow:0 3px 6px rgba(0,0,0,.25);display:flex;align-items:center;color:#fff;font-size:17px;font-weight:500}
.tile.active{background:var(--blue)}
.tile-icon{width:65px;height:51px;display:flex;align-items:center;justify-content:center;border-right:1px solid rgba(255,255,255,.35)}
.tile.active .tile-icon{border-right:1px solid var(--red)}
.tile-label{padding-left:16px;flex:1}
.tile-arrow{margin-right:18px}

/* news */
.section-title{position:absolute;left:0;width:1200px;text-align:center;font-size:25px;font-weight:500;color:#444;letter-spacing:.5px}
.news-card{position:absolute;top:799px;width:309px}
.news-photo{width:309px;height:214px}
.news-title{margin-top:14px;font-size:13.4px;font-weight:500;line-height:21px;color:#333;padding-left:1px;white-space:nowrap}
.news-text{margin-top:8px;font-size:11px;line-height:22px;color:var(--body);font-weight:300}
.hair{position:absolute;left:0;top:1124px;width:1200px;height:1px;background:var(--line);z-index:-1}

/* work with us */
.work{position:absolute;left:0;top:1221px;width:1200px;height:333px;background:linear-gradient(160deg,#f3f3f3,#ececec 50%,#f6f6f6)}
.work-text{position:absolute;left:0;top:128px;width:1200px;text-align:center;font-size:13px;line-height:23px;color:#444;font-weight:300}
.btn{position:absolute;background:var(--blue);color:#fff;display:flex;align-items:center;justify-content:center;font-weight:500}
.btn-start{left:480px;top:196px;width:240px;height:51px;font-size:16px}

/* social + newsletter */
.social{position:absolute;top:1633px;width:50px;height:50px;border:2px solid #b5b5b5;border-radius:50%;display:flex;align-items:center;justify-content:center;font-size:16px;font-weight:500;color:#aaa}
.mail-input{position:absolute;left:390px;top:1729px;width:300px;height:43px;background:#ececec;font-size:11px;color:#999;padding:14px 14px}
.btn-signup{left:699px;top:1729px;width:111px;height:43px;font-size:12.5px}
.footer-line{position:absolute;left:0;top:1832px;width:1200px;height:1px;background:var(--line)}

/* contact */
.contact-title{position:absolute;left:111px;top:1868px;font-size:19px;font-weight:500;color:#333}
.contact-row{position:absolute;left:111px;display:flex;gap:10px;font-size:11.3px;line-height:22px;color:#444}
.contact-row .ic{width:14px;display:flex;justify-content:center;padding-top:4px}
.contact-row.phone{font-size:14px;font-weight:500}
.hours{position:absolute;left:111px;top:2045px;width:350px;height:34px;background:#ececec;display:flex;align-items:center;gap:14px;padding-left:12px;font-size:13.5px;color:#333}
.map{position:absolute;left:496px;top:1875px;width:463px;height:214px;background:linear-gradient(135deg,#ece8df,#e4e0d6 50%,#ede9e1)}
.copyright{position:absolute;left:0;top:2121px;width:1200px;text-align:center;font-size:11px;color:#555}
</style>
</head>
<body>

<header class="site-header">
  <div class="brand">
    <span class="brand-mark"></span>
    <span class="brand-name">Kolrev</span>
  </div>
  <div class="call">
    <svg width="24" height="24" viewBox="0 0 24 24"><path d="M6 3l4 4-2 3c1 2 3 4 5 5l3-2 4 4-3 3C10 20 4 14 3 6z" fill="var(--blue)"/></svg>
    CALL US: <strong>010-4471920</strong>
  </div>
  <span class="vsep" style="left:798px"></span>
  <div class="search">Type Here
    <svg width="18" height="18" viewBox="0 0 18 18"><circle cx="7.5" cy="7.5" r="6" fill="none" stroke="var(--blue)" stroke-width="2"/><path d="M12 12l5 5" stroke="var(--blue)" stroke-width="2"/></svg>
  </div>
  <span class="vsep" style="left:1000px"></span>
  <div class="menu">
    <svg width="30" height="20" viewBox="0 0 30 20"><path d="M0 2h30M0 10h30M0 18h30" stroke="var(--green)" stroke-width="2"/></svg>
    Menu
  </div>
</header>

<section class="hero" role="img" aria-label="Photo of hands holding a small potted cactus in soil">
  <h1 class="hero-title">WE CREATE SUSTAINABLE PATHWAYS<br>TO A BETTER FUTURE</h1>
</section>

<nav class="tiles">
  <a class="tile active" style="left:111px;top:45px">
    <span class="tile-icon"><svg width="36" height="32" viewBox="0 0 36 32" fill="none" stroke="#fff" stroke-width="1.4"><rect x="2" y="12" width="22" height="18"/><rect x="24" y="4" width="8" height="26"/><path d="M6 17h4M13 17h4M6 23h4M13 23h4M2 30h32"/></svg></span>
    <span class="tile-label">HVB</span>
    <svg class="tile-arrow" width="26" height="10" viewBox="0 0 26 10"><path d="M0 5h24M19 1l5 4-5 4" fill="none" stroke="#fff" stroke-width="1.3"/></svg>
  </a>
  <a class="tile" style="left:445px;top:45px">
    <span class="tile-icon"><svg width="36" height="32" viewBox="0 0 36 32" fill="none" stroke="#fff" stroke-width="1.4"><rect x="2" y="12" width="22" height="18"/><rect x="24" y="4" width="8" height="26"/><path d="M6 17h4M13 17h4M6 23h4M13 23h4M2 30h32"/></svg></span>
    <span class="tile-label">Stodboende</span>
    <svg class="tile-arrow" width="26" height="10" viewBox="0 0 26 10"><path d="M0 5h24M19 1l5 4-5 4" fill="none" stroke="#fff" stroke-width="1.3"/></svg>
  </a>
  <a class="tile" style="left:779px;top:45px">
    <span class="tile-icon"><svg width="36" height="32" viewBox="0 0 36 32" fill="none" stroke="#fff" stroke-width="1.4"><rect x="3" y="3" width="30" height="26" rx="2"/><path d="M8 23l7-7 5 4 9-9"/></svg></span>
    <span class="tile-label">Oppenvard</span>
    <svg class="tile-arrow" width="26" height="10" viewBox="0 0 26 10"><path d="M0 5h24M19 1l5 4-5 4" fill="none" stroke="#fff" stroke-width="1.3"/></svg>
  </a>
  <a class="tile" style="left:111px;top:121px">
    <span class="tile-icon"><svg width="34" height="34" viewBox="0 0 34 34" fill="none" stroke="#fff" stroke-width="1.4"><circle cx="17" cy="17" r="15"/><circle cx="17" cy="17" r="6"/><path d="M17 2v9M17 23v9M2 17h9M23 17h9"/></svg></span>
    <span class="tile-label">Vir behendsting</span>
    <svg class="tile-arrow" width="26" height="10" viewBox="0 0 26 10"><path d="M0 5h24M19 1l5 4-5 4" fill="none" stroke="#fff" stroke-width="1.3"/></svg>
  </a>
  <a class="tile" style="left:445px;top:121px">
    <span class="tile-icon"><svg width="34" height="34" viewBox="0 0 34 34" fill="none" stroke="#fff" stroke-width="1.4"><circle cx="17" cy="11" r="7"/><path d="M4 32c0-8 6-12 13-12s13 4 13 12z"/></svg></span>
    <span class="tile-label">Own Iss</span>
    <svg class="tile-arrow" width="26" height="10" viewBox="0 0 26 10"><path d="M0 5h24M19 1l5 4-5 4" fill="none" stroke="#fff" stroke-width="1.3"/></svg>
  </a>
  <a class="tile" style="left:779px;top:121px">
    <span class="tile-icon"><svg width="36" height="34" viewBox="0 0 36 34" fill="none" stroke="#fff" stroke-width="1.4"><path d="M4 8h22l6 6-6 6H4z"/><path d="M13 20v13M19 20v13"/></svg></span>
    <span class="tile-label">Piacering</span>
    <svg class="tile-arrow" width="26" height="10" viewBox="0 0 26 10"><path d="M0 5h24M19 1l5 4-5 4" fill="none" stroke="#fff" stroke-width="1.3"/></svg>
  </a>
</nav>

<h2 class="section-title" style="top:727px">LATEST NEWS</h2>
<span class="hair"></span>

<article class="news-card" style="left:111px">
  <div class="news-photo" role="img" aria-label="Photo of young people at an indoor go-kart track" style="background:linear-gradient(135deg,#5a5d5c,#8c8a82 50%,#3e4040)"></div>
  <h3 class="news-title">Evidence-based methods, higcompetence<br>and overall experience</h3>
  <p class="news-text">Sed diam nonummy nibh euismod tincidunt ut laoreet dolore magna aliquam erat volutpatt enim ad minim veniam quis nostrud exerci tatullamco suscipit lobortis nisl ut aliquip...</p>
</article>
<article class="news-card" style="left:445px">
  <div class="news-photo" role="img" aria-label="Photo of two people in winter jackets and helmets at a go-kart hall" style="background:linear-gradient(135deg,#6a6b68,#8e8d86 45%,#2a2c30)"></div>
  <h3 class="news-title">Evidence-based methods, higcompetence<br>and overall experience</h3>
  <p class="news-text">Sed diam nonummy nibh euismod tincidunt ut laoreet dolore magna aliquam erat volutpatt enim ad minim veniam quis nostrud exerci tatullamco suscipit lobortis nisl ut aliquip...</p>
</article>
<article class="news-card" style="left:779px">
  <div class="news-photo" role="img" aria-label="Photo of a hand cutting food on a kitchen counter" style="background:linear-gradient(160deg,#3a2f2b,#9a8f86 40%,#b3aba2 70%,#6e645c)"></div>
  <h3 class="news-title">Evidence-based methods, higcompetence<br>and overall experience</h3>
  <p class="news-text">Sed diam nonummy nibh euismod tincidunt ut laoreet dolore magna aliquam erat volutpatt enim ad minim veniam quis nostrud exerci tatullamco suscipit lobortis nisl ut aliquip...</p>
</article>

<section class="work">
  <h2 class="section-title" style="top:82px">WORK WITH US</h2>
  <p class="work-text">Want to become a part of a business on the move with the vision<br>of being the best?</p>
  <a class="btn btn-start">GET STARTED NOW</a>
</section>

<a class="social" style="left:489px">Fb</a>
<a class="social" style="left:575px">Yt</a>
<a class="social" style="left:662px">In</a>

<div class="mail-input">Enter Your Mail Id:</div>
<a class="btn btn-signup">SIGN UP</a>

<span class="footer-line"></span>

<h2 class="contact-title">Contact Us</h2>
<div class="contact-row" style="top:1900px">
  <span class="ic"><svg width="12" height="18" viewBox="0 0 12 18"><path d="M6 0a6 6 0 016 6c0 4-6 12-6 12S0 10 0 6a6 6 0 016-6z" fill="var(--blue)"/><circle cx="6" cy="6" r="2" fill="#fff"/></svg></span>
  <span>Kolrev Sverige AB Ekbacka 22<br>241 36 Lindås</span>
</div>
<div class="contact-row phone" style="top:1954px">
  <span class="ic"><svg width="14" height="14" viewBox="0 0 24 24"><path d="M6 3l4 4-2 3c1 2 3 4 5 5l3-2 4 4-3 3C10 20 4 14 3 6z" fill="var(--blue)"/></svg></span>
  <span>010-4471920</span>
</div>
<div class="contact-row" style="top:1985px">
  <span class="ic"><svg width="14" height="10" viewBox="0 0 14 10"><rect width="14" height="10" fill="var(--blue)"/><path d="M0 0l7 5 7-5" fill="none" stroke="#fff" stroke-width="1.2"/></svg></span>
  <span>info@kolrev.se<br>Org nr 556123-4587</span>
</div>
<div class="hours">
  <svg width="20" height="20" viewBox="0 0 20 20" fill="none" stroke="#999" stroke-width="1.3"><rect x="1" y="3" width="18" height="16"/><path d="M1 8h18M5 1v4M15 1v4M5 12h2M9 12h2M13 12h2M5 15h2M9 15h2"/></svg>
  Monday - Friday 09:00 - 18:00
</div>
<div class="map" role="img" aria-label="Street map showing the office location"></div>

<p class="copyright">© All Rights Reserved. 2018</p>

</body>
</html>
```